Real Estate Agent need a business card

I am a real estate agent in Vancouver, BC Canada. I recently used PixelHarbor to develop a logo of my own. I would like to have my logo in the business card, as well my realty office logo also must be displayed along with its address. I also would like to have my headshot photo displayed in the business card on both sides.

Industry/Entity Type

Real Estate Agent

Contact Information for Business Card

My office address:
Bramwell Peak Realty
2271 Lindqvist St.
Vancouver, BC V5K 2P8

My contact information:
Cell: 604-555-0148
Office: 604-555-0192
Fax: 604-555-0193

My website : www.danielmorvik.example
My email: email@danielmorvik.example

My slogan: Simply I do. Far and Above.

Requirements
Must have
• Front side(all in colour): My photo, My own logo, My office logo, My cell number, My website address and email, My slogan.
• Back side(could be black & white/ plz refer to the file name "preview"): My photo, My own logo, my office logo, my office address, my contact information.
• * Please read this: Since my logo has my name in it, there is no need to put my name in the card separately. As well, my office logo MUST BE displayed on both sides(you can reduce the size of office logo). But the office address can be displayed only one side, front or back. I would prefer to have my cell number only to be displayed prominently on the front side. So all the numbers should be displayed on the backside instead. Remember that I am trying to promote myself so the most important thing I consider from the front side of the card is my cell number, my website, and my email, not the office. The only thing I require by industry regulation from the front side is my office logo. Hope this helps.
Nice to have
• Colour on the front side and the black and white on the back side

```html
<!DOCTYPE html>
<html lang="en">
<head>
<meta charset="utf-8">
<title>Daniel Morvik – Business Card</title>
<link href="https://fonts.googleapis.com/css2?family=Montserrat:wght@700;800&family=Open+Sans:ital,wght@0,400;0,600;0,700;1,300;1,400&display=swap" rel="stylesheet">
<style>
  :root{
    --backdrop:#3b2619;
    --green:#7dc242;
    --charcoal:#4a4b4d;
    --ring:#404143;
    --white:#ffffff;
    --text-dark:#3a3b3d;
    --night-top:#2b2d9c;
    --night-teal:#1c8c8a;
    --night-city:#1c1f5e;
    --mono-sky:#9a9a9a;
    --mono-city:#4d4d4d;
  }
  *{margin:0;padding:0;box-sizing:border-box}
  html,body{width:1200px;height:1200px;overflow:hidden}
  body{background:var(--backdrop);position:relative;font-family:"Open Sans",sans-serif}

  .card{position:absolute;left:125px;width:950px;height:543px;overflow:hidden;background:var(--white)}
  .card--front{top:38px}
  .card--back{top:620px}

  .scene{position:absolute;inset:0}
  .scene--night{
    background:
      linear-gradient(200deg, var(--night-teal) 0%, rgba(28,140,138,0) 40%),
      linear-gradient(180deg, var(--night-top) 0%, #2a3a9a 28%, var(--night-city) 60%, #15184a 100%);
  }
  .scene--mono{
    background:linear-gradient(180deg, #a7a7a7 0%, var(--mono-sky) 35%, #6e6e6e 55%, var(--mono-city) 80%, #3a3a3a 100%);
    height:398px;bottom:auto;
  }

  .tagline{position:absolute;color:var(--white);font-style:italic;font-weight:300;white-space:nowrap}
  .card--front .tagline{top:40px;left:0;width:950px;text-align:center;font-size:38px}
  .card--back .tagline{top:76px;font-size:30px}
  .tagline--left{left:48px}
  .tagline--right{right:44px}

  .slogan{position:absolute;top:104px;left:0;width:950px;text-align:center;color:var(--white);font-style:italic;font-weight:400;font-size:20px;letter-spacing:.5px}

  .band{position:absolute;left:0;width:950px}
  .band__rule{position:absolute;left:0;width:950px;height:10px;background:var(--charcoal)}
  .band__rule::before{content:"";position:absolute;left:0;top:0;height:10px;background:var(--green)}

  .card--front .band{top:352px;height:103px;background:var(--white)}
  .card--front .band__rule--top{top:0}
  .card--front .band__rule--bottom{bottom:0}
  .card--front .band__rule::before{width:467px}

  .agent-mark{position:absolute;left:30px;top:24px;display:flex;align-items:center;gap:16px}
  .agent-mark__square{width:50px;height:50px;background:var(--charcoal)}
  .agent-mark__name{font-family:"Montserrat",sans-serif;font-weight:800;font-size:33px;color:var(--text-dark);letter-spacing:.5px;line-height:1}
  .agent-mark__role{font-family:"Montserrat",sans-serif;font-weight:700;font-size:14px;color:var(--green);letter-spacing:4.2px;margin-top:6px;margin-left:34px}

  .cell{position:absolute;left:432px;top:36px;display:flex;align-items:center;gap:8px;color:var(--text-dark);font-weight:700;font-size:22px;white-space:nowrap}
  .cell__icon{width:22px;height:22px;fill:var(--green)}

  .front-contact{position:absolute;left:30px;top:470px;color:var(--white);font-size:15px;line-height:1.6;white-space:nowrap}
  .front-contact__office{display:flex;align-items:center;gap:8px;font-weight:700}
  .front-contact__dot{width:12px;height:12px;border-radius:50%;background:var(--white)}

  .headshot{position:absolute;border-radius:50%;background:var(--ring);display:flex;align-items:center;justify-content:center}
  .headshot__ring{border-radius:50%;background:var(--green);display:flex;align-items:center;justify-content:center}
  .headshot__photo{border-radius:50%;background:radial-gradient(circle at 50% 40%, #e6cdb9 0%, #bfa596 35%, #6f7f73 70%, #2b3448 100%)}
  .card--front .headshot{left:710px;top:302px;width:208px;height:208px}
  .card--front .headshot__ring{width:172px;height:172px}
  .card--front .headshot__photo{width:156px;height:156px}
  .card--back .headshot{left:401px;top:30px;width:148px;height:148px}
  .card--back .headshot__ring{width:126px;height:126px}
  .card--back .headshot__photo{width:110px;height:110px}

  .card--back .band__rule{top:398px;height:8px}
  .card--back .band__rule::before{width:458px;height:8px}

  .office-mark{position:absolute;left:70px;top:460px;display:flex;align-items:center;gap:10px}
  .office-mark__dot{width:16px;height:16px;border-radius:50%;background:var(--text-dark)}
  .office-mark__name{font-weight:700;font-size:19px;color:var(--text-dark)}

  .office-details{position:absolute;left:474px;top:422px;color:var(--text-dark);white-space:nowrap}
  .office-details__name{font-weight:700;font-size:20px;letter-spacing:.3px;line-height:1.35}
  .office-details__line{font-weight:400;font-size:16px;line-height:1.4}
</style>
</head>
<body>

<section class="card card--front" aria-label="Card front">
  <div class="scene scene--night" role="img" aria-label="Night aerial photo of Vancouver city towers and harbour lights"></div>
  <p class="tagline">Your&nbsp; Real Estate Agent in Vancouver, Canada.</p>
  <p class="slogan">Simply I do. Far and Above.</p>
  <div class="band">
    <div class="band__rule band__rule--top"></div>
    <div class="agent-mark">
      <div class="agent-mark__square"></div>
      <div>
        <div class="agent-mark__name">DANIEL MORVIK</div>
        <div class="agent-mark__role">REAL ESTATE AGENT</div>
      </div>
    </div>
    <p class="cell">
      <svg class="cell__icon" viewBox="0 0 24 24" aria-hidden="true"><path d="M6.6 10.8a15.1 15.1 0 0 0 6.6 6.6l2.2-2.2a1 1 0 0 1 1-.25 11.4 11.4 0 0 0 3.6.57 1 1 0 0 1 1 1V20a1 1 0 0 1-1 1A17 17 0 0 1 3 4a1 1 0 0 1 1-1h3.5a1 1 0 0 1 1 1c0 1.25.2 2.45.57 3.57a1 1 0 0 1-.25 1z"/></svg>
      604-555-0148
    </p>
    <div class="band__rule band__rule--bottom"></div>
  </div>
  <div class="front-contact">
    <p>www.danielmorvik.example&nbsp;&nbsp;|&nbsp;&nbsp;email@danielmorvik.example</p>
    <p class="front-contact__office"><span class="front-contact__dot"></span>Bramwell Peak Realty</p>
  </div>
  <div class="headshot">
    <div class="headshot__ring">
      <div class="headshot__photo" role="img" aria-label="Headshot photo of the agent"></div>
    </div>
  </div>
</section>

<section class="card card--back" aria-label="Card back">
  <div class="scene scene--mono" role="img" aria-label="Black and white aerial photo of Vancouver residential towers"></div>
  <p class="tagline tagline--left">Your&nbsp; Real Estate Agent</p>
  <p class="tagline tagline--right">in Vancouver, Canada.</p>
  <div class="headshot">
    <div class="headshot__ring">
      <div class="headshot__photo" role="img" aria-label="Headshot photo of the agent"></div>
    </div>
  </div>
  <div class="band__rule"></div>
  <div class="office-mark">
    <span class="office-mark__dot"></span>
    <span class="office-mark__name">Bramwell Peak Realty</span>
  </div>
  <div class="office-details">
    <p class="office-details__name">BRAMWELL PEAK REALTY</p>
    <p class="office-details__line">2271 Lindqvist St., Vancouver, BC V5K 2P8</p>
    <p class="office-details__line">Cell: 604-555-0148&nbsp;&nbsp;·&nbsp;&nbsp;Office: 604-555-0192</p>
    <p class="office-details__line">Fax: 604-555-0193</p>
  </div>
</section>

</body>
</html>
```